Adelaide based cleaning and remediation business needs a website design

We are launching a new company with no clients as yet so we don't have the benefit of Veltrano Ratings to build confidence. We can use our  past work history with other employers in the industry to give some credibility. Happy to use any colour scheme as long as it look interesting when people click on the site it gets there attention. enquiry . I have supplied a mock up the important information and various photos as they tell a lot of the story.

```html
<!DOCTYPE html>
<html lang="en">
<head>
<meta charset="utf-8">
<title>Karrawin Services — Cleaning &amp; Remediation Adelaide</title>
<link href="https://fonts.googleapis.com/css2?family=Archivo+Black&family=Poppins:wght@400;500;600;700&display=swap" rel="stylesheet">
<style>
:root{
  --blue:#2b57a8;
  --blue-dark:#1e418a;
  --orange:#f47a42;
  --ink:#1f2430;
  --text:#4a4f5a;
  --grey-bg:#f2f2f3;
  --line:#e1e3e8;
  --footer:#1c2230;
  --white:#ffffff;
}
*{box-sizing:border-box;margin:0;padding:0}
html,body{width:1200px;height:4669px;overflow:hidden;background:var(--white)}
body{position:relative;font-family:"Poppins",sans-serif;color:var(--text)}
.abs{position:absolute}
.heading{font-family:"Archivo Black",sans-serif;color:var(--blue);font-size:31px;letter-spacing:.5px;text-transform:uppercase;text-align:center;width:1200px;left:0}
.btn{position:absolute;display:flex;align-items:center;gap:12px;background:var(--orange);color:#fff;border-radius:26px;height:42px;padding:0 6px 0 24px;font-size:12px;font-weight:600;letter-spacing:.4px;text-transform:uppercase}
.btn .arr{width:32px;height:32px;border-radius:50%;background:#fff;display:flex;align-items:center;justify-content:center}
.photo{position:absolute;border-radius:8px}

/* header */
.site-header{position:absolute;left:0;top:0;width:1200px;height:102px;background:#fff}
.brand{position:absolute;left:141px;top:24px;display:flex;align-items:center;gap:10px;color:var(--blue);font-weight:700;font-size:22px;line-height:1}
.brand .dot{width:34px;height:34px;border-radius:50%;background:var(--blue)}
.brand small{display:block;font-size:12px;letter-spacing:1px;margin-top:3px}
.nav{position:absolute;top:41px;left:382px;display:flex;gap:30px;font-size:12px;font-weight:500;color:var(--ink);text-transform:uppercase}
.nav .active{color:var(--blue)}

/* hero */
.hero-title{left:141px;top:222px;font-family:"Archivo Black",sans-serif;color:#fff;font-size:48px;line-height:64px}
.hero-sub{left:141px;top:424px;color:#fff;font-size:17px;line-height:26px}

/* services */
.card{position:absolute;top:885px;width:298px;height:395px;border-radius:10px;overflow:hidden}
.card .cap{position:absolute;left:24px;right:20px;bottom:28px;color:#fff}
.card h3{font-family:"Archivo Black",sans-serif;font-size:20px;line-height:25px;text-transform:uppercase;margin-bottom:14px}
.card p{font-size:12.5px;line-height:20px;margin-bottom:14px}
.card .link{display:flex;align-items:center;gap:12px;font-size:12px;font-weight:600}
.card .link span{width:26px;height:26px;border-radius:50%;background:var(--orange);display:flex;align-items:center;justify-content:center}

/* why */
.why-bg{left:0;top:1372px;width:1200px;height:568px;background:var(--grey-bg)}
.why-title{left:144px;top:1466px;font-family:"Archivo Black",sans-serif;color:var(--blue);font-size:31px;text-transform:uppercase}
.why-list{left:141px;top:1530px;width:380px;list-style:none;font-size:13px;line-height:21px;color:var(--ink)}
.why-list li{position:relative;padding-left:26px;margin-bottom:9px}
.why-list li svg{position:absolute;left:0;top:3px}

/* process */
.process-bg{left:0;top:2647px;width:1200px;height:526px;background:var(--grey-bg)}
.step{position:absolute;top:2797px;width:230px;text-align:center}
.step .ring{width:106px;height:106px;border-radius:50%;border:1.5px solid var(--line);background:#fff;margin:0 auto;position:relative;display:flex;align-items:center;justify-content:center}
.step .num{position:absolute;left:0;top:0;width:26px;height:26px;border-radius:50%;background:var(--orange);color:#fff;font-size:12px;display:flex;align-items:center;justify-content:center}
.step h4{font-size:17px;font-weight:500;color:var(--ink);margin-top:12px}
.step p{font-size:12.5px;line-height:19px;margin-top:8px}
.step-arrow{position:absolute;top:2843px;color:#b8bcc6;font-size:18px}

/* faq */
.faq{position:absolute;width:448px;height:52px;background:#fff;border-left:3px solid var(--blue);box-shadow:0 2px 14px rgba(30,40,70,.1);display:flex;align-items:center;justify-content:space-between;padding:0 24px;font-size:14px;font-weight:500;color:var(--ink)}
.faq b{font-size:22px;font-weight:400}
.faq.open{background:var(--blue);color:#fff}
.faq-answer{position:absolute;left:611px;top:3376px;width:448px;height:66px;background:#fff;box-shadow:0 6px 14px rgba(30,40,70,.08);padding:14px 20px;font-size:12.5px;line-height:21px}

/* inquiry */
.inquiry{left:236px;top:3756px;width:739px;height:450px;background:#fff;border-top:5px solid var(--blue);border-radius:8px;box-shadow:0 6px 30px rgba(30,40,70,.1)}
.field{position:absolute;height:43px;border:1px solid var(--line);border-radius:4px;display:flex;align-items:center;gap:14px;padding-left:14px;font-size:11.5px;color:var(--text)}

/* footer */
.footer{left:0;top:4255px;width:1200px;height:414px;background:linear-gradient(180deg,#2a3142 0%,#1c2230 60%,#181d28 100%)}
.foot-h{font-family:"Archivo Black",sans-serif;color:#fff;font-size:18px;text-transform:uppercase;top:4320px}
.foot-list{list-style:none;color:#d9dce3;font-size:13px;line-height:27px}
.contact-item{color:#fff;font-size:12.5px;line-height:19px;padding-left:24px;position:relative}
.contact-item strong{display:block;font-size:12px;font-weight:600}
.contact-item svg{position:absolute;left:0;top:2px}
.social{display:flex;align-items:center;gap:12px;color:#fff;font-size:13px;margin-bottom:18px}
.social span{width:28px;height:28px;border-radius:50%;border:1px solid #fff}
.social span.on{background:var(--orange);border-color:var(--orange)}
.copy{left:0;top:4634px;width:1200px;text-align:center;color:#c9ccd4;font-size:11.5px}
</style>
</head>
<body>

<header class="site-header">
  <div class="brand"><span class="dot"></span><div>KARRAWIN<small>SERVICES</small></div></div>
  <nav class="nav">
    <span class="active">Home</span><span>Services</span><span>Why Choose Us</span><span>Work</span><span>Process</span><span style="text-transform:none">FAQs</span>
  </nav>
  <div class="btn" style="left:906px;top:30px;height:40px">Contact us<span class="arr"><svg width="12" height="12" viewBox="0 0 12 12"><path d="M3 9L9 3M4 3h5v5" stroke="#f47a42" stroke-width="1.4" fill="none"/></svg></span></div>
</header>

<section class="hero">
  <div class="abs" role="img" aria-label="Cluttered storage room full of hoarded items and debris" style="left:0;top:102px;width:1200px;height:660px;background:linear-gradient(120deg,#2b2520 0%,#5a4a38 40%,#8a7458 60%,#3a3228 100%)"></div>
  <svg class="abs" style="left:0;top:102px" width="1200" height="680" viewBox="0 0 1200 680">
    <path d="M0 490 C150 600 330 650 520 630 C760 605 980 540 1200 525 L1200 680 L0 680 Z" fill="#fff"/>
    <path d="M185 612 C330 680 470 672 620 630 C770 590 900 540 1015 522 C900 548 780 600 630 645 C480 690 320 690 185 612 Z" fill="#2b57a8"/>
  </svg>
  <h1 class="abs hero-title">We Do The Dirty<br>Jobs Nobody<br>Wants To Do</h1>
  <p class="abs hero-sub">Professional cleaning &amp; remediation services<br>in Adelaide</p>
  <div class="btn" style="left:141px;top:494px">Get a free quote<span class="arr"><svg width="12" height="12" viewBox="0 0 12 12"><path d="M3 9L9 3M4 3h5v5" stroke="#f47a42" stroke-width="1.4" fill="none"/></svg></span></div>
</section>

<section class="services">
  <h2 class="abs heading" style="top:818px">Our Services</h2>
  <div class="card" style="left:141px">
    <div class="abs" role="img" aria-label="Worker in protective suit clearing an estate" style="inset:0;background:linear-gradient(180deg,#5d6c7c 0%,#3a4350 50%,#12161c 100%)"></div>
    <div class="cap"><h3>Estate Cleanups</h3><p>Lorem ipsum dolor sit a consectetuer<br>adipiscing elit sed diam nonummy.</p><div class="link">CONTACT US<span><svg width="10" height="10" viewBox="0 0 12 12"><path d="M3 9L9 3M4 3h5v5" stroke="#fff" stroke-width="1.5" fill="none"/></svg></span></div></div>
  </div>
  <div class="card" style="left:451px">
    <div class="abs" role="img" aria-label="Worker in respirator removing pigeon waste" style="inset:0;background:linear-gradient(180deg,#3c3d3c 0%,#55564f 45%,#141414 100%)"></div>
    <div class="cap"><h3>Pigeon Waste<br>Cleanups</h3><div class="link">CONTACT US<span><svg width="10" height="10" viewBox="0 0 12 12"><path d="M3 9L9 3M4 3h5v5" stroke="#fff" stroke-width="1.5" fill="none"/></svg></span></div></div>
  </div>
  <div class="card" style="left:761px">
    <div class="abs" role="img" aria-label="Fire damaged kitchen with exposed ceiling insulation" style="inset:0;background:linear-gradient(180deg,#7a6a64 0%,#4a4644 50%,#121212 100%)"></div>
    <div class="cap"><h3>Fire Damage<br>Cleanouts</h3><div class="link">CONTACT US<span><svg width="10" height="10" viewBox="0 0 12 12"><path d="M3 9L9 3M4 3h5v5" stroke="#fff" stroke-width="1.5" fill="none"/></svg></span></div></div>
  </div>
</section>

<section class="why">
  <div class="abs why-bg"></div>
  <h2 class="abs why-title">Why Choose Us?</h2>
  <ul class="abs why-list">
    <li><svg width="15" height="15" viewBox="0 0 16 16"><circle cx="8" cy="8" r="8" fill="#2b57a8"/><path d="M4.5 8.2l2.3 2.3 4.7-4.8" stroke="#fff" stroke-width="1.6" fill="none"/></svg>Our team brings over 20 years of experience in the cleaning and remediation industry, having worked on numerous projects with leading employers.</li>
    <li><svg width="15" height="15" viewBox="0 0 16 16"><circle cx="8" cy="8" r="8" fill="#2b57a8"/><path d="M4.5 8.2l2.3 2.3 4.7-4.8" stroke="#fff" stroke-width="1.6" fill="none"/></svg>Certified in Mould Remediation (ICRTB Standard S520)</li>
    <li><svg width="15" height="15" viewBox="0 0 16 16"><circle cx="8" cy="8" r="8" fill="#2b57a8"/><path d="M4.5 8.2l2.3 2.3 4.7-4.8" stroke="#fff" stroke-width="1.6" fill="none"/></svg>ICRTB Standard Trauma &amp; Crime Scene Cleaning</li>
    <li><svg width="15" height="15" viewBox="0 0 16 16"><circle cx="8" cy="8" r="8" fill="#2b57a8"/><path d="M4.5 8.2l2.3 2.3 4.7-4.8" stroke="#fff" stroke-width="1.6" fill="none"/></svg>National Police Cleared &amp; Working with Vulnerable People (DHS)</li>
    <li><svg width="15" height="15" viewBox="0 0 16 16"><circle cx="8" cy="8" r="8" fill="#2b57a8"/><path d="M4.5 8.2l2.3 2.3 4.7-4.8" stroke="#fff" stroke-width="1.6" fill="none"/></svg>Fully Insured for $20 Million Public Liability</li>
    <li><svg width="15" height="15" viewBox="0 0 16 16"><circle cx="8" cy="8" r="8" fill="#2b57a8"/><path d="M4.5 8.2l2.3 2.3 4.7-4.8" stroke="#fff" stroke-width="1.6" fill="none"/></svg>Compassionate approach for sensitive hoarding cases</li>
  </ul>
  <div class="btn" style="left:141px;top:1798px">Get a free quote<span class="arr"><svg width="12" height="12" viewBox="0 0 12 12"><path d="M3 9L9 3M4 3h5v5" stroke="#f47a42" stroke-width="1.4" fill="none"/></svg></span></div>
  <div class="photo" role="img" aria-label="Vandalised hoarder house interior with debris and graffiti" style="left:566px;top:1465px;width:494px;height:384px;background:linear-gradient(135deg,#7a6e62 0%,#9a8a76 40%,#5a4e44 100%)"></div>
</section>

<section class="works">
  <h2 class="abs heading" style="top:2025px">Our Works</h2>
  <div class="photo" role="img" aria-label="Roof cavity covered in bird droppings" style="left:141px;top:2147px;width:254px;height:230px;background:linear-gradient(160deg,#3a3632,#7a7268,#2e2a26)"></div>
  <div class="photo" role="img" aria-label="Shelves packed with hoarded goods" style="left:199px;top:2393px;width:196px;height:161px;background:linear-gradient(160deg,#5a4030,#9a7a58,#3a3028)"></div>
  <div class="photo" role="img" aria-label="Worker in protective suit cleaning a rooftop box gutter" style="left:408px;top:2090px;width:382px;height:397px;background:linear-gradient(180deg,#8a9098 0%,#c8c0b0 35%,#3c3a38 100%)"></div>
  <div class="photo" role="img" aria-label="Warehouse floor covered in waste" style="left:801px;top:2101px;width:156px;height:138px;background:linear-gradient(160deg,#5c5a48,#8a866c,#4a4838)"></div>
  <div class="photo" role="img" aria-label="Pigeons nesting on a stained ledge" style="left:801px;top:2248px;width:258px;height:263px;background:linear-gradient(180deg,#e4e4e2 0%,#d0ccc4 55%,#a89880 100%)"></div>
</section>

<section class="process">
  <div class="abs process-bg"></div>
  <h2 class="abs heading" style="top:2730px">Our Process</h2>
  <div class="step" style="left:126px"><div class="ring"><span class="num">01</span><svg width="46" height="46" viewBox="0 0 46 46" fill="none" stroke="#2b57a8" stroke-width="2"><rect x="8" y="8" width="24" height="30" rx="2"/><path d="M14 16h4M14 24h4M14 32h4M22 16h5M22 24h5M22 32h5"/><path d="M36 14l4 4-10 14-5 1 1-5z"/></svg></div><h4>Assessment</h4><p>Lorem ipsum dolor sit amet<br>consectetuer adipiscing elit<br>sed diam nonummy.</p></div>
  <div class="step-arrow" style="left:354px">→</div>
  <div class="step" style="left:365px"><div class="ring"><span class="num">02</span><svg width="46" height="46" viewBox="0 0 46 46" fill="none" stroke="#2b57a8" stroke-width="2"><path d="M10 6h18l8 8v26H10z"/><path d="M16 20h14M16 27h8"/><path d="M38 22l4 4-12 12-5 1 1-5z"/></svg></div><h4>Quote</h4><p>Lorem ipsum dolor sit amet<br>consectetuer adipiscing elit<br>sed diam nonummy.</p></div>
  <div class="step-arrow" style="left:592px">→</div>
  <div class="step" style="left:605px"><div class="ring"><span class="num">03</span><svg width="46" height="46" viewBox="0 0 46 46" fill="none" stroke="#2b57a8" stroke-width="2"><path d="M38 6L24 22"/><path d="M18 20l10 10-8 12c-6-2-12-8-14-14z"/><path d="M12 8v4M10 10h4M30 36h4M32 34v4"/></svg></div><h4>Cleaning</h4><p>Lorem ipsum dolor sit amet<br>consectetuer adipiscing elit<br>sed diam nonummy.</p></div>
  <div class="step-arrow" style="left:831px">→</div>
  <div class="step" style="left:844px"><div class="ring"><span class="num">04</span><svg width="46" height="46" viewBox="0 0 46 46" fill="none" stroke="#2b57a8" stroke-width="2"><circle cx="27" cy="19" r="12"/><path d="M21 19l4 4 8-8"/><path d="M18 28L7 39"/></svg></div><h4>Inspection</h4><p>Lorem ipsum dolor sit amet<br>consectetuer adipiscing elit<br>sed diam nonummy.</p></div>
  <div class="btn" style="left:520px;top:3037px">Get started<span class="arr"><svg width="12" height="12" viewBox="0 0 12 12"><path d="M3 9L9 3M4 3h5v5" stroke="#f47a42" stroke-width="1.4" fill="none"/></svg></span></div>
</section>

<section class="faqs">
  <h2 class="abs heading" style="top:3254px">Frequently Asked Questions</h2>
  <div class="faq" style="left:141px;top:3323px">Ut enim ad minim veniam quis nostrud.<b>+</b></div>
  <div class="faq" style="left:141px;top:3392px">Ut enim ad minim veniam quis nostrud.<b>+</b></div>
  <div class="faq" style="left:141px;top:3461px">Ut enim ad minim veniam quis nostrud.<b>+</b></div>
  <div class="faq" style="left:141px;top:3531px">Ut enim ad minim veniam quis nostrud.<b>+</b></div>
  <div class="faq open" style="left:611px;top:3324px">Ut enim ad minim veniam quis nostrud.<b>−</b></div>
  <div class="faq-answer">Ut enim ad minim veniam, quis nostrud exercitation ulla laboris nisi ut aliquip ex ea commodo consequat.</div>
  <div class="faq" style="left:611px;top:3461px">Ut enim ad minim veniam quis nostrud.<b>+</b></div>
  <div class="faq" style="left:611px;top:3531px">Ut enim ad minim veniam quis nostrud.<b>+</b></div>
  <div class="btn" style="left:520px;top:3623px">Get started<span class="arr"><svg width="12" height="12" viewBox="0 0 12 12"><path d="M3 9L9 3M4 3h5v5" stroke="#f47a42" stroke-width="1.4" fill="none"/></svg></span></div>
</section>

<section class="abs inquiry">
  <h2 class="abs heading" style="top:58px;width:739px">Quick Inquiry</h2>
  <p class="abs" style="top:104px;width:739px;text-align:center;font-size:12.5px;color:var(--ink)">Ut enim ad minim veniam, quis nostrud exercitation ullamco laboris nisi ut aliquip ex.</p>
  <div class="field" style="left:72px;top:134px;width:290px"><svg width="12" height="12" viewBox="0 0 12 12" fill="#2b57a8"><circle cx="6" cy="3.5" r="3"/><path d="M0 12c0-4 3-5 6-5s6 1 6 5z"/></svg>First Name*</div>
  <div class="field" style="left:379px;top:134px;width:288px"><svg width="12" height="12" viewBox="0 0 12 12" fill="#2b57a8"><circle cx="6" cy="3.5" r="3"/><path d="M0 12c0-4 3-5 6-5s6 1 6 5z"/></svg>Last Name*</div>
  <div class="field" style="left:72px;top:191px;width:290px"><svg width="12" height="12" viewBox="0 0 12 12" fill="#2b57a8"><path d="M2 0l3 3-1.5 2a7 7 0 0 0 3.5 3.5L9 7l3 3-2 2C5 12 0 7 0 2z"/></svg>Your Phone*</div>
  <div class="field" style="left:379px;top:191px;width:288px"><svg width="12" height="10" viewBox="0 0 12 10" fill="#2b57a8"><path d="M0 0h12v10H0z"/><path d="M0 0l6 5 6-5" stroke="#fff" fill="none"/></svg>Your Email*</div>
  <div class="field" style="left:72px;top:247px;width:595px;height:83px;align-items:flex-start;padding-top:14px"><svg width="13" height="11" viewBox="0 0 13 11" fill="#2b57a8"><ellipse cx="5" cy="4" rx="5" ry="3.6"/><ellipse cx="9" cy="7" rx="4" ry="3"/></svg>Your Message</div>
  <div class="btn" style="left:285px;top:364px">Submit now<span class="arr"><svg width="12" height="12" viewBox="0 0 12 12"><path d="M3 9L9 3M4 3h5v5" stroke="#f47a42" stroke-width="1.4" fill="none"/></svg></span></div>
</section>

<footer class="abs footer" role="img" aria-label="Dim city skyline behind footer content"></footer>
<div class="abs foot-h" style="left:143px">Quick Links</div>
<ul class="abs foot-list" style="left:143px;top:4366px">
  <li>• Home</li><li>• Services</li><li>• Why Choose Us</li><li>• Work</li><li>• Process</li><li>• FAQs</li><li>• Contact Us</li>
</ul>
<div class="abs foot-h" style="left:355px">Contact Details</div>
<div class="abs" style="left:355px;top:4366px">
  <div class="contact-item"><svg width="12" height="14" viewBox="0 0 12 14" fill="#fff"><path d="M6 0a6 6 0 0 0-6 6c0 4 6 8 6 8s6-4 6-8a6 6 0 0 0-6-6zm0 8.5A2.5 2.5 0 1 1 6 3.5a2.5 2.5 0 0 1 0 5z"/></svg><strong>ADDRESS</strong>123 Ut enim ad mini veniam<br>quis nostrud exercita.</div>
  <div class="contact-item" style="margin-top:14px"><svg width="12" height="12" viewBox="0 0 12 12" fill="#fff"><path d="M2 0l3 3-1.5 2a7 7 0 0 0 3.5 3.5L9 7l3 3-2 2C5 12 0 7 0 2z"/></svg><strong>PHONE</strong>(123) 456-7890</div>
  <div class="contact-item" style="margin-top:22px"><svg width="12" height="10" viewBox="0 0 12 10" fill="#fff"><path d="M0 0h12v10H0z"/><path d="M0 0l6 5 6-5" stroke="#1c2230" fill="none"/></svg><strong>EMAIL</strong>info@karrawinservices.com</div>
</div>
<div class="abs foot-h" style="left:652px">Follow Us</div>
<div class="abs" style="left:652px;top:4372px">
  <div class="social"><span class="on"></span>Socialia</div>
  <div class="social"><span></span>Vidstream</div>
  <div class="social"><span></span>Snapgram</div>
  <div class="social"><span></span>Chirp.com</div>
</div>
<div class="abs" style="left:860px;top:4410px;display:flex;align-items:center;gap:14px;color:#fff;font-weight:700;font-size:32px;line-height:1">
  <span style="width:40px;height:40px;border-radius:50%;background:#fff"></span>
  <div>KARRAWIN<div style="font-size:20px;letter-spacing:1px;margin-top:6px">SERVICES</div></div>
</div>
<div class="abs" style="left:0;top:4614px;width:1200px;height:1px;background:rgba(255,255,255,.12)"></div>
<p class="abs copy">© 2025 Karrawin Services. All Rights Reserved.</p>

</body>
</html>
```